Free range pig farm business

We'd like a simple but elegant website for our new free range pig farm business.
Check out www.kellowridgeporkers.com.au and http://www.toravinefields.com.au/
pages:
Home
About
Shop
Contact
Target Market(s)
People who would want to find out where they could buy our pork
Industry/Entity Type
Agribusiness
Number of Pages Required
4 page
Font styles to use
Other font styles liked:
- As per our logo
Requirements
Must have
- Ability for us to update weekly with new news and photos

```html
<!DOCTYPE html>
<html lang="en">
<head>
<meta charset="utf-8">
<title>Greenhollow Pastured Pork</title>
<link rel="stylesheet" href="https://fonts.googleapis.com/css2?family=PT+Sans:wght@400;700&family=Open+Sans:wght@400;600&display=swap">
<style>
:root{
  --lime:#a3c93a;
  --forest:#2d5127;
  --cocoa:#4e3534;
  --ink:#222;
  --muted:#888;
  --white:#fff;
}
*{box-sizing:border-box;margin:0;padding:0}
html,body{width:890px;height:1200px;overflow:hidden;background:var(--white)}
body{position:relative;font-family:"Open Sans",sans-serif;color:var(--ink)}
.abs{position:absolute}
.head{font-family:"PT Sans",sans-serif}
.topbar .call{left:530px;top:8px;font-size:10px;color:var(--muted);display:flex;align-items:center;gap:5px}
.topbar .call b{font-weight:400;color:#333;font-size:10.5px}
.social{top:2px;width:26px;height:26px}
.social.s1{left:688px;background:#3b5998}
.social.s2{left:717px;background:#1da1f2}
.social.s3{left:746px;background:#dd4b39}
.nav-strip{left:0;top:30px;width:113px;height:30px;background:var(--lime)}
.nav{left:274px;top:30px;width:616px;height:30px;background:var(--lime);display:flex;align-items:center}
.nav a{font-family:"PT Sans",sans-serif;font-size:10px;font-weight:700;color:#1d2a12;text-decoration:none;letter-spacing:.3px;margin-left:26px}
.nav a:first-child{margin-left:26px}
.search{left:611px;top:36px;width:160px;height:18px;background:var(--white)}
.brand{left:114px;top:40px;width:160px;height:130px;display:flex;flex-direction:column;align-items:center}
.brand .dot{width:44px;height:44px;border-radius:50%;background:var(--forest);margin-top:8px}
.brand .name{font-family:"PT Sans",sans-serif;font-size:13px;color:var(--ink);text-align:center;line-height:1.3;margin-top:14px}
.block{position:absolute}
.lime{background:var(--lime)}
.forest{background:var(--forest)}
.cocoa{background:var(--cocoa)}
.tile-title{font-family:"PT Sans",sans-serif;color:var(--white);font-weight:700;display:flex;align-items:center}
.about{padding:12px 14px;color:var(--white)}
.about h3{font-family:"PT Sans",sans-serif;font-weight:400;font-size:13px;margin-bottom:6px}
.about p{font-size:7px;line-height:12px}
.about .more{font-size:6.5px;font-weight:600;margin-top:6px;display:block}
.intro h2{position:absolute;left:0;width:890px;top:446px;text-align:center;font-family:"PT Sans",sans-serif;font-size:22px;font-weight:700;letter-spacing:.3px}
.intro p{position:absolute;left:118px;width:630px;top:483px;text-align:center;font-size:8.4px;line-height:14.4px;color:#333}
.cta{top:574px;height:37px;width:209px;display:flex;align-items:center;justify-content:space-between;padding:0 10px 0 20px;font-family:"PT Sans",sans-serif;font-size:19px;color:var(--white)}
.cta svg{flex:none}
.banner{left:0;top:648px;width:890px;height:137px;background:linear-gradient(180deg,#5a403a,#4e3a33 60%,#54443a)}
.banner p{position:absolute;top:30px;width:890px;text-align:center;color:var(--white);font-size:12px}
.shop-btn{left:342px;top:715px;width:184px;height:33px;border-radius:17px;background:var(--lime);color:var(--white);font-family:"PT Sans",sans-serif;font-weight:700;font-size:12px;display:flex;align-items:center;justify-content:center}
.testi-title{left:0;width:890px;top:830px;text-align:center;font-family:"PT Sans",sans-serif;font-size:22px;font-weight:700}
.quote{color:var(--white);font-size:7.8px;line-height:14.4px}
.q1{left:158px;top:890px;width:284px;height:150px;padding:24px 22px}
.q2{left:443px;top:912px;width:284px;height:110px;padding:22px 20px}
.tail{position:absolute;width:0;height:0;border-top:12px solid}
.avatar{border-radius:50%}
.person .n{font-family:"Open Sans",sans-serif;font-size:10px;color:#333}
.person .r{font-size:7.5px;color:#999;margin-top:4px}
.footer{left:0;top:1172px;width:890px;height:28px;background:var(--cocoa);color:var(--white);font-size:7.5px;display:flex;align-items:center;justify-content:center}
</style>
</head>
<body>

<header class="topbar">
  <div class="abs call">Call Us:
    <svg width="11" height="11" viewBox="0 0 24 24"><path fill="#7cbf2c" d="M6.6 10.8a15 15 0 0 0 6.6 6.6l2.2-2.2c.3-.3.7-.4 1-.2 1.1.4 2.3.6 3.6.6.6 0 1 .4 1 1V20c0 .6-.4 1-1 1A17 17 0 0 1 3 4c0-.6.4-1 1-1h3.5c.6 0 1 .4 1 1 0 1.3.2 2.5.6 3.6.1.3 0 .7-.2 1z"/></svg>
    <b>+1 555 0142 677</b></div>
  <span class="abs social s1" aria-label="Social link"></span>
  <span class="abs social s2" aria-label="Social link"></span>
  <span class="abs social s3" aria-label="Social link"></span>
</header>

<div class="abs nav-strip"></div>
<nav class="abs nav">
  <a href="#">HOME</a><a href="#">ABOUT US</a><a href="#">SHOP</a><a href="#">CONTACT US</a>
</nav>
<div class="abs search">
  <svg class="abs" style="left:145px;top:3px" width="12" height="12" viewBox="0 0 24 24"><circle cx="10" cy="10" r="7" fill="none" stroke="#222" stroke-width="3"/><path d="M15 15l6 6" stroke="#222" stroke-width="3"/></svg>
</div>

<div class="abs brand">
  <span class="dot"></span>
  <div class="name">GREENHOLLOW PASTURED<br>PORK</div>
</div>

<!-- mosaic -->
<div class="block forest" style="left:0;top:62px;width:110px;height:232px"></div>
<div class="block lime" role="img" aria-label="Faint tree and field motif" style="left:774px;top:64px;width:116px;height:230px;background:linear-gradient(135deg,#a3c93a,#97bf34)"></div>

<div class="block" role="img" aria-label="Family kneeling with piglets on a green pasture" style="left:278px;top:64px;width:327px;height:112px;background:linear-gradient(180deg,#6f7a55,#5f8a3a 55%,#6c9a3c)"></div>
<div class="block cocoa tile-title" style="left:610px;top:64px;width:160px;height:112px;padding-left:11px;font-size:24px;font-weight:400;line-height:1.25">FREE RANGE<br>PIG FARM</div>

<div class="block" role="img" aria-label="Butcher cutting a cut of pork on a board" style="left:114px;top:182px;width:160px;height:112px;background:linear-gradient(160deg,#d8d2cc,#b58a7c 60%,#8d5f50)"></div>
<div class="block lime tile-title" style="left:278px;top:182px;width:160px;height:112px;justify-content:center;font-size:26px;font-weight:400">THE PORK</div>
<div class="block" role="img" aria-label="Young pigs looking at the camera in a barn" style="left:444px;top:182px;width:161px;height:112px;background:linear-gradient(180deg,#5d4b3f,#c8a69a 55%,#8a6a55)"></div>
<div class="block" role="img" aria-label="Sow feeding piglets in an open field" style="left:610px;top:182px;width:160px;height:112px;background:linear-gradient(180deg,#9aa7a8,#b78d7f 45%,#8a7a55)"></div>

<div class="block cocoa" style="left:0;top:300px;width:110px;height:113px"></div>
<div class="block lime tile-title" style="left:114px;top:300px;width:159px;height:113px;padding-left:18px;font-size:26px;font-weight:400">GALLERY</div>
<div class="block" role="img" aria-label="Farmer feeding pigs in a pen" style="left:278px;top:300px;width:160px;height:113px;background:linear-gradient(135deg,#3a3a3a,#c9a095 50%,#2f8a3a)"></div>
<div class="block forest about" style="left:444px;top:300px;width:326px;height:113px">
  <h3>ABOUT GREENHOLLOW PASTURED PORK</h3>
  <p>Lorem Ipsum is simply dummy text of the printing and typesetting industry. Lorem Ipsum has been the industry's standard dummy text ever since the 1500s, when an unknown printer took a galley of type and scrambled it to make a type specimen book. It has survived not only five centuries.</p>
  <span class="more">READ MORE →</span>
</div>
<div class="block cocoa" style="left:774px;top:300px;width:116px;height:113px"></div>

<section class="intro">
  <h2>GREENHOLLOW PASTURED PORK</h2>
  <p>simply dummy text of the printing and typesetting industry. Lorem Ipsum has been the industry's standard dummy text ever since the 1500s, when an unknown printer took a galley of type and scrambled it to make a type specimen book. It has survived not only five centuries, but also the leap into electronic typesetting, remaining essentially unchanged. It was popularised in the 1960s with the release of Letraset sheets containing Lorem Ipsum passages, and more recently with desktop publishing software like Aldus PageMaker including versions of Lorem Ipsum.</p>
</section>

<a class="abs cta cocoa" style="left:111px">Free range pig
  <svg width="20" height="20" viewBox="0 0 20 20"><circle cx="10" cy="10" r="9" fill="#eee"/><path d="M5 10h9M10 6l4 4-4 4" fill="none" stroke="#333" stroke-width="1.8"/></svg></a>
<a class="abs cta lime" style="left:336px">Our Gallery
  <svg width="20" height="20" viewBox="0 0 20 20"><circle cx="10" cy="10" r="9" fill="#eee"/><path d="M5 10h9M10 6l4 4-4 4" fill="none" stroke="#333" stroke-width="1.8"/></svg></a>
<a class="abs cta forest" style="left:563px">Pastured Pork
  <svg width="20" height="20" viewBox="0 0 20 20"><circle cx="10" cy="10" r="9" fill="#eee"/><path d="M5 10h9M10 6l4 4-4 4" fill="none" stroke="#333" stroke-width="1.8"/></svg></a>

<section class="abs banner" role="img" aria-label="Dimmed photo of a family with pigs on the farm">
  <p>Lorem Ipsum has been the industry's standard dummy text ever since the 1500s, when an unknown</p>
</section>
<div class="abs shop-btn">OUR FARM SHOP</div>

<h2 class="abs testi-title">CLIENT TESTIMONIALS</h2>

<div class="abs quote lime q1">simply dummy text of the printing and typesetting industry. Lorem Ipsum has been the industry's standard dummy text ever since the 1500s, when an unknown printer took a galley of type and scrambled it to make a type specimen book. It has survived not only five centuries, but also the leap into electronic typesetting, remaining essentially unchanged.</div>
<span class="tail" style="left:210px;top:1040px;border-top-color:var(--lime);border-right:14px solid transparent"></span>
<div class="abs quote forest q2">simply dummy text of the printing and typesetting industry. Lorem Ipsum has been the industry's standard dummy text ever since the 1500s, when an unknown printer took a galley of type and scrambled it to make a type specimen book.</div>
<span class="tail" style="left:653px;top:1022px;border-top-color:var(--forest);border-left:13px solid transparent"></span>

<div class="abs avatar" role="img" aria-label="Portrait of a client holding a camera" style="left:173px;top:1075px;width:64px;height:64px;background:radial-gradient(circle at 50% 45%,#e8c2a8,#6b4a38)"></div>
<div class="abs person" style="left:254px;top:1094px"><div class="n">Mara Ellis</div><div class="r">CEO and Founder</div></div>
<div class="abs avatar" role="img" aria-label="Portrait of a client" style="left:649px;top:1054px;width:64px;height:64px;background:radial-gradient(circle at 50% 45%,#e9cdb8,#5a3c2c)"></div>
<div class="abs person" style="left:530px;top:1073px;width:102px;text-align:right"><div class="n">Jodie</div><div class="r">Account Managar</div></div>

<footer class="abs footer">Copyright © 2016 Greenhollow Pastured Pork . All Rights Reserved</footer>

</body>
</html>
```